Re-design of 4 x 2-sided reports

I need the 4 attached reports (3 are 2-sides of A4; 1 is 7-sides of A4) to be re-designed with a consistent look and feel. Just need 1 or 2 images per report being inserted plus consistent branding and contact details being displayed in the same location on each report with same colour, font and design). Reports are attached.
The reports are used as lead magnets.
That is, visitors to our website can download one of them (7 Steps To Sharpen Your Sales Over The Coming Month) by filling in a form with their email address. Then over the next 30 days the other reports are sent to the subscriber via email autoresponders.
Blue Harbour Marketing is a marketing consultancy dealing with companies in the North West of England providing cost-effective and profitable marketing to small and medium-sized businesses that want better and quicker results. The reports need to be professional and corporate looking. Please let me know if you need any further clarification or have any questions. I attach an example report. I don't necessarily want to mirror this report (from the law firm) but it may help to understand what look I'm trying to get. Many thanks, Gordon

Target Market(s)

SMEs based in NW of England
Typically with turnover of £1m to £10m or 10 to 100 employees
Clients often in the construction sector, healthcare, accountants, lawyers and local councils.

Industry/Entity Type

Marketing

Font styles to use
Serif
Sans Serif

Colors
ec1f27

Requirements
Must have
• Consistent branding
• Logo in same place across all four reports
• Contact details in same place across all four reports
• Same font across all four reports
• Same colour across all four reports
• Professional and bold look
Nice to have
• Some strong stock photography
• 1 or 2 images per report
• More images for the 7-page report though
Should not have
• No graphics

```html
<!DOCTYPE html>
<html lang="en">
<head>
<meta charset="utf-8">
<title>10 Quick &amp; Easy Ways To Grow Your Business Using Social Media</title>
<link href="https://fonts.googleapis.com/css2?family=Montserrat:wght@300;500;600&family=Open+Sans:wght@400&display=swap" rel="stylesheet">
<style>
  :root {
    --brand-red: #c4122f;
    --brand-deep: #7f1a2a;
    --header-grey: #efefef;
    --ink: #333333;
    --paper: #ffffff;
    --backdrop: #e9e4dc;
  }
  * { box-sizing: border-box; margin: 0; padding: 0; }
  html, body { width: 1200px; height: 1200px; overflow: hidden; background: var(--backdrop); }
  .report {
    position: absolute; left: 193px; top: 25px;
    width: 884px; height: 1250px;
    background: var(--paper);
    transform: scale(0.92); transform-origin: top left;
    box-shadow: 0 6px 18px rgba(0,0,0,.18);
    font-family: "Open Sans", Arial, sans-serif; color: var(--ink);
  }
  .report-header {
    position: absolute; left: 0; top: 0; width: 100%; height: 135px;
    background: var(--header-grey);
  }
  .brand {
    position: absolute; left: 50px; top: 48px;
    display: flex; align-items: center; gap: 12px;
    font-family: "Montserrat", Arial, sans-serif; font-weight: 600;
    font-size: 25px; color: var(--brand-red); line-height: 1.1;
  }
  .brand-mark { width: 34px; height: 34px; background: var(--brand-red); flex: none; }
  .header-title {
    position: absolute; left: 416px; top: 32px; width: 420px;
    font-family: "Montserrat", Arial, sans-serif; font-weight: 500;
    font-size: 23.5px; line-height: 29px; color: var(--brand-red);
  }
  .header-rule {
    position: absolute; left: 416px; top: 106px; width: 417px; height: 2px;
    background: var(--brand-deep);
  }
  .column { position: absolute; top: 185px; width: 375px; font-size: 17.4px; line-height: 21.4px; }
  .column-left { left: 50px; }
  .column-right { left: 467px; }
  .kicker, .report-title {
    font-family: "Montserrat", Arial, sans-serif; font-weight: 500; color: var(--brand-red);
  }
  .kicker { font-size: 20px; line-height: 26px; }
  .report-title { font-size: 26.5px; line-height: 32px; margin-bottom: 18px; }
  .steps { padding-left: 21px; }
  .steps ol { list-style-type: lower-alpha; padding-left: 21px; }
  .continued { padding-left: 42px; }
  .report-footer {
    position: absolute; left: 0; bottom: 0; width: 100%; height: 102px;
    background: var(--brand-deep); color: #f4dede; text-align: center;
    font-family: "Montserrat", Arial, sans-serif; font-weight: 300;
    font-size: 17px; line-height: 23px; padding-top: 26px;
  }
</style>
</head>
<body>
<article class="report">
  <header class="report-header">
    <div class="brand"><span class="brand-mark"></span><span>Blue Harbour Marketing</span></div>
    <h2 class="header-title">10 Quick &amp; Easy Ways To Grow Your Business Using Social Media</h2>
    <div class="header-rule"></div>
  </header>

  <section class="column column-left">
    <p class="kicker">FREE REPORT:</p>
    <h1 class="report-title">10 Quick &amp; Easy Ways To Grow Your Business Using Social Media</h1>
    <ol class="steps">
      <li>Decide what social media platforms to use for your business
        <ol>
          <li>If you sell to other businesses, you will need to have a Company Profile on Linkwell.</li>
          <li>If you sell to the public (consumers) you will almost certainly want to be on Friendly.</li>
          <li>Whether you are business-to-business (B2B) or business-to-consumer (B2C) you will also need to have a SearchHub Page and a corporate Chatter account.</li>
          <li>If your business lends itself to video having a corporate ViewStream account could also be very valuable.</li>
        </ol>
      </li>
      <li>Decide on what you want to achieve from social media.
        <ol>
          <li>Set objectives that will help the business. Otherwise, you can end up doing social media for no discernable benefit.</li>
          <li>An example is to 'increase the number of visitors to your website by 30% in the next 6 months' or 'drive sales via social media by £x p.a. by displaying y number of products p.m.'.</li>
        </ol>
      </li>
      <li>Decide on how you want your business to be seen on social media i.e. what's your social media brand - formal, corporate, fun, provocative, educational or other?
        <ol>
          <li>Ensure that your posts reflect your desired social media brand.</li>
        </ol>
      </li>
      <li>Decide on who will take a lead and 'do your social media'.
        <ol>
          <li>Typically, that can be someone in-</li>
        </ol>
      </li>
    </ol>
  </section>

  <section class="column column-right">
    <p class="continued">house (if they have the skills) or someone from outside such as a freelancer or social media consultant (which avoids the risks and costs of employing someone specifically to do this work).</p>
    <ol class="steps" start="5">
      <li>Commit to posting regularly.
        <ol>
          <li>Results won't necessarily come instantly and social media requires that 'you give before you get'.</li>
          <li>Start with 2 to 3 posts per week and work up to 1 per day.</li>
        </ol>
      </li>
      <li>Add links in your posts to certain pages of your website in order to drive traffic to your website to increase the likelihood of enquiries and/or sales.</li>
      <li>Ask the people that follow you on social media questions in order to try to start a conversation with them, rather than just 'broadcast' or 'sell' to them in every post.
        <ol>
          <li>People want interesting and valuable content rather than just being sold to.</li>
        </ol>
      </li>
      <li>Understand social media etiquette:
        <ol>
          <li>be respectful to all, be polite, be solution-focused, be nice, act in a helpful manner, don't slag off your competition and try to 'talk' to your followers rather than just 'sell' to them.</li>
        </ol>
      </li>
      <li>Brainstorm ideas for content with as many people in your business as possible.
        <ol>
          <li>Encourage them to make ideas on an ongoing basis. They will probably come up with the best ideas!</li>
        </ol>
      </li>
      <li>Join relevant groups and answer questions in order to showcase your expertise. This will eventually generate enquiries and sales leads.</li>
    </ol>
  </section>

  <footer class="report-footer">
    <p>Copyright @ Blue Harbour Marketing</p>
    <p>www.blueharbourmarketing.co.uk |01632 960 418 | hello@blueharbourmarketing.co.uk</p>
  </footer>
</article>
</body>
</html>
```